'TOLVANTA' NEW WINE LABEL DESIGN

I am looking for an exceptional and exciting design for a wine label called 'Tolvanta' meaning 'Lookout'. The design must feature the name 'Tolvanta', and the word 'Cabernet Sauvignon' in version 1 and 'Sauvignon Blanc' in version 2. It will also need the words 'Valle Central, Chile' at the bottom of the label as a prominent piece of information as well as the vintage 2017. Please produce the work in size 80mm x 100mm. Feel free to use colour in addition to black/white and ensue that the label is easy to read on a shelf placement.
Target Market(s)
SUPERMARKETS & WINE STORES
Requirements
Must have
- EASY TO READ, USE COLOURS LIKE GREEN FOR SAUVIGNON & RED FOR CABERNET SAUVIGNON
- FULL BOTTLE SHOT MUST BE IN PROVIDED DESIGNS. ALL BOTTLE TOPS SHOULD BE QUORLAN STYLE (SCREW TOP)
- PLEASE NOTE THAT LABEL INFORMATION MUSY BE EASY TO READ I.E. VINTAGE, PLACE OF ORGIN ALTHOUGH NOT THE MAIN CONTENT MUST STILL BE CLEAR.
Nice to have
- ARTISTIC REFERENCE LINK TO NAME & ANDES BUT NOT PICTURES OF MOUNTAINS
Should not have
- PICTURES OF GRAPES
- PICTURES OF VINEYARDS
- PICTURES OF MOUNTAINS

```html
<!DOCTYPE html>
<html lang="en">
<head>
<meta charset="utf-8">
<title>Tolvanta – Cabernet Sauvignon Label</title>
<link rel="stylesheet" href="https://fonts.googleapis.com/css2?family=Jost:wght@300;400;700&display=swap">
<style>
  :root {
    --paper: #ffffff;
    --ink: #111111;
    --wine-red: #9e1b12;
    --wine-red-soft: #ecd2cf;
  }
  html, body {
    margin: 0;
    padding: 0;
    overflow: hidden;
    background: var(--paper);
  }
  .label {
    position: relative;
    width: 1200px;
    height: 1000px;
    overflow: hidden;
    background: var(--paper);
    font-family: "Jost", "Century Gothic", sans-serif;
    color: var(--ink);
  }
  .ridge-artwork {
    position: absolute;
    left: 0;
    top: 15px;
    width: 600px;
    height: 980px;
    background: linear-gradient(200deg, var(--wine-red-soft) 0%, #d99a94 45%, var(--wine-red) 100%);
    clip-path: polygon(20% 0%, 66% 18%, 98% 58%, 82% 83%, 25% 100%, 0% 100%, 0% 9%);
    opacity: 0.9;
  }
  .brand-name {
    position: absolute;
    right: 450px;
    top: 208px;
    margin: 0;
    font-weight: 400;
    font-size: 86px;
    line-height: 1;
    letter-spacing: 1px;
    color: var(--ink);
    transform: translateX(450px);
    text-align: right;
  }
  .varietal {
    position: absolute;
    right: 452px;
    top: 590px;
    margin: 0;
    font-weight: 300;
    font-size: 48px;
    line-height: 56px;
    text-align: right;
    transform: translateX(450px);
    color: var(--ink);
  }
  .origin {
    position: absolute;
    right: 452px;
    top: 800px;
    margin: 0;
    text-align: right;
    transform: translateX(450px);
    font-weight: 700;
    line-height: 1;
  }
  .origin-region {
    display: block;
    font-size: 32px;
    font-variant: small-caps;
    letter-spacing: 0.5px;
  }
  .origin-country {
    display: block;
    margin-top: 10px;
    font-size: 34px;
    letter-spacing: 0.5px;
  }
  .vintage {
    position: absolute;
    right: 452px;
    top: 896px;
    margin: 0;
    transform: translateX(450px);
    font-weight: 700;
    font-size: 22px;
    line-height: 1;
    text-align: right;
  }
  .vintage-word {
    font-variant: small-caps;
    font-size: 20px;
    letter-spacing: 1px;
  }
</style>
</head>
<body>
  <main class="label">
    <div class="ridge-artwork" role="img" aria-label="Red hatched line artwork of descending ridge lines suggesting a lookout over the Andes"></div>

    <h1 class="brand-name">TOLVANTA</h1>

    <p class="varietal">CABERNET<br>SAUVIGNON</p>

    <p class="origin">
      <span class="origin-region">Valle Central</span>
      <span class="origin-country">CHILE</span>
    </p>

    <p class="vintage"><span class="vintage-word">vintage</span> 2017</p>
  </main>
</body>
</html>
```